Label / Packaging design for supplements bottle (capsule bottle)

We are a startup supplements company focusing on animal nutrition. The task here is to design the supplement bottles for the product series. Think of bodybuilding supplement packaging more than health&wellness type of packaging.

The brandname is Perch Dynamics

The goal is to have 3 bottles with similar/identical designs but with different color accents (i.e. red for one bottle, yellow for the second, (not green or blue) for the third).

The bottles can either be black theme or white theme. I'll leave it up to the designer.

Final design should communicate bodybuilding (bold fonts preferred)

Logo files below (both SVG and AI files), the insignia can be used independently of the text and slogan, or it can be positioned above brand name or beside it.
*Feel free to change the color of the insignia and text to match your chosen accent color for the bottle!*

Bottle size will be approximately 11.9cm x 6.35cm (Height x circumference) (height is from bottom to mouth opening)
Thus, label size at the moment can be designed 6.30cm x 10cm (L x W)

Target Market(s)

Male, Adult

Industry/Entity Type

It Company

Font styles to use
Sans Serif

Requirements
Must have
• Text: "Performance Enhancing Supplements for Racing Pigeons"
• Essentials
• "240 Capsules"
• Bottle 1:
• Creatine+Carnitine
• Text + Imagery:*see Carnitine Benefits.png
• Bottle 2:
• BCAA
• Text:
• SUPPORT MUSCLE PROTEIN SYNTHESIS
• DECREASE PROTEIN CATABOLISM
• PROMOTE INSULIN SENSITIVITY
• Offset Muscle Breakdown and Increase Muscular Endurance
• ENHANCED RECOVERY FROM EXERCISE
• Promotes Lowered Body Fat Levels, Increased Strength, & Improves Muscle Repair
• (Imagery can use the same as bottle 1 similar to Carnitine Benefits.png)
• Bottle 3:
• Vitamins
• Text: Supports Rigorous Training and Needs To Support Growth and Overall Well-being
• Spaces for Text for:
• 1.) Directions for Use
• 2.) Developed by:
• 3.) Ingredients
Nice to have
• Mosaic/Pattern subtle fading background (e.g. honeycomb etc)
• Prominent "A" "B" "C" on each bottle,
• A for Bulwark Nutrients
• B for BCAA
• C for Taurine/Glutamine Complex
• XYZ Essential Series

```html
<!DOCTYPE html>
<html lang="en">
<head>
<meta charset="utf-8">
<title>Perch Dynamics – Creatine + Carnitine Label</title>
<link rel="stylesheet" href="https://fonts.googleapis.com/css2?family=Bebas+Neue&family=Exo+2:ital,wght@0,700;1,600&family=Barlow+Condensed:ital,wght@1,500&family=Barlow:wght@300;400;700&display=swap">
<style>
  :root {
    --stage: #68cbe0;
    --orange: #f26b22;
    --peach: #fde3d2;
    --ink: #111111;
    --paper: #ffffff;
    --hex-edge: #d9d9d9;
  }
  * { margin: 0; padding: 0; box-sizing: border-box; }
  html, body { width: 1200px; height: 740px; overflow: hidden; }
  body { background: var(--stage); position: relative; font-family: "Barlow", sans-serif; }

  .label {
    position: absolute; left: 157px; top: 78px; width: 887px; height: 558px;
    background: var(--paper);
    box-shadow: 26px 26px 22px rgba(0, 0, 0, 0.55);
    overflow: hidden;
  }
  .pattern-area { position: absolute; }
  .pattern-top {
    left: 400px; top: 0; width: 221px; height: 160px;
    background: radial-gradient(ellipse at 70% 40%, var(--peach) 0%, rgba(253,227,210,0.5) 45%, rgba(255,255,255,0) 75%);
  }
  .pattern-corner {
    left: 0; top: 0; width: 110px; height: 120px;
    background: radial-gradient(ellipse at 20% 40%, var(--peach) 0%, rgba(255,255,255,0) 70%);
  }
  .pattern-bottom {
    left: 0; top: 355px; width: 621px; height: 203px;
    background: linear-gradient(180deg, rgba(255,255,255,0) 0%, rgba(253,227,210,0.55) 60%, var(--peach) 100%);
  }

  .brand-plate { position: absolute; left: 105px; top: 0; width: 236px; height: 86px; }
  .brand-name {
    position: absolute; left: 105px; top: 34px; width: 236px; text-align: center;
    font-family: "Exo 2", sans-serif; font-weight: 700; font-size: 19px;
    letter-spacing: 0.5px; color: var(--ink);
  }

  .initial-mark { position: absolute; left: 0; top: 132px; width: 621px; height: 222px; }

  .product-title { position: absolute; left: 155px; top: 130px; width: 280px; height: 150px; }
  .title-text { font-family: "Bebas Neue", sans-serif; font-size: 94px; }

  .tagline {
    position: absolute; left: 155px; top: 288px;
    font-family: "Exo 2", sans-serif; font-style: italic; font-weight: 600;
    font-size: 28.5px; line-height: 32px; color: var(--ink); letter-spacing: 0.6px;
  }

  .benefit-icons { position: absolute; left: 0; top: 360px; width: 340px; height: 198px; }
  .hex-label { font-family: "Barlow", sans-serif; font-size: 13px; fill: var(--paper); text-anchor: middle; }
  .hex-label-large { font-size: 15px; }
  .hex-label-small { font-size: 12.5px; }
  .count-number { font-family: "Barlow", sans-serif; font-weight: 700; font-size: 44px; fill: var(--paper); letter-spacing: -1px; }
  .count-unit { font-family: "Barlow", sans-serif; font-size: 18px; fill: var(--paper); letter-spacing: -0.3px; }

  .benefit-list { position: absolute; left: 337px; top: 372px; list-style: none; }
  .benefit-list li {
    position: relative; padding-left: 20px; height: 25px; line-height: 25px;
    font-family: "Barlow Condensed", sans-serif; font-style: italic; font-weight: 500;
    font-size: 21.5px; color: var(--ink); letter-spacing: -0.2px;
  }
  .benefit-list li::before {
    content: ""; position: absolute; left: 0; top: 5px; width: 13px; height: 16px;
    background: var(--orange);
    clip-path: polygon(0 0, 50% 0, 100% 50%, 50% 100%, 0 100%, 50% 50%);
  }

  .info-panel { position: absolute; left: 621px; top: 0; width: 266px; height: 558px; background: var(--orange); }
  .info-notch { position: absolute; left: 598px; top: 271px; width: 24px; height: 83px; background: var(--orange); }
  .info-heading {
    position: absolute; left: 28px; font-family: "Barlow", sans-serif; font-weight: 300;
    font-size: 21px; color: var(--paper);
  }
  .info-directions { top: 43px; }
  .info-ingredients { top: 233px; }
  .info-developer { top: 474px; }
</style>
</head>
<body>
  <div class="label">
    <div class="pattern-area pattern-corner" role="img" aria-label="Faint peach honeycomb pattern"></div>
    <div class="pattern-area pattern-top" role="img" aria-label="Faint peach honeycomb pattern"></div>
    <div class="pattern-area pattern-bottom" role="img" aria-label="Faint peach honeycomb pattern fading upward"></div>

    <svg class="brand-plate" viewBox="0 0 236 86" aria-hidden="true">
      <polygon points="0,0 236,0 198,86 38,86" fill="var(--orange)"/>
    </svg>
    <div class="brand-name">PERCH DYNAMICS</div>

    <svg class="initial-mark" viewBox="0 0 621 222" aria-hidden="true">
      <path d="M0,139 H49 V42 Q49,0 92,0 H126 Q143,0 143,17 V62 H107 V40 Q107,28 95,28 H94 Q83,28 83,40 V186 Q83,198 94,198 H95 Q107,198 107,186 V156 H143 V205 Q143,222 126,222 H0 Z" fill="var(--orange)"/>
    </svg>

    <svg class="product-title" viewBox="0 0 280 150" aria-label="Creatine + Carnitine">
      <text class="title-text" x="0" y="68" fill="var(--ink)" textLength="272" lengthAdjust="spacingAndGlyphs">CREATINE+</text>
      <text class="title-text" x="0" y="142" fill="var(--orange)" textLength="254" lengthAdjust="spacingAndGlyphs">CARNITINE</text>
    </svg>

    <p class="tagline">Performance Enhancing<br>Supplements for Racing Pigeons</p>

    <svg class="benefit-icons" viewBox="0 0 340 198">
      <!-- capsule count plate -->
      <polygon class="count-plate" points="0,94 107,94 127,158 111,198 0,198" fill="var(--orange)"/>
      <text class="count-number" x="12" y="154">240</text>
      <text class="count-unit" x="12" y="180">CAPSULES</text>

      <g stroke="var(--hex-edge)" stroke-width="4" fill="var(--orange)">
        <polygon points="16,52 40,10 86,10 110,52 86,94 40,94"/>
        <polygon points="85,94 109,52 155,52 179,94 155,136 109,136"/>
        <polygon points="154,50 178,8 224,8 248,50 224,92 178,92"/>
        <polygon points="224,92 248,50 294,50 318,92 294,134 248,134"/>
      </g>

      <!-- dumbbell -->
      <g fill="var(--paper)">
        <rect x="43" y="30" width="5" height="16" rx="1"/>
        <rect x="49" y="26" width="6" height="24" rx="1"/>
        <rect x="55" y="35" width="16" height="6"/>
        <rect x="71" y="26" width="6" height="24" rx="1"/>
        <rect x="78" y="30" width="5" height="16" rx="1"/>
      </g>
      <text class="hex-label" x="63" y="68">Build</text>
      <text class="hex-label" x="63" y="82">Muscle</text>

      <!-- flame -->
      <path d="M132,64 C138,71 142,76 142,82 C142,88 137,92 132,92 C127,92 122,88 122,82 C122,77 126,74 127,69 C129,73 130,75 131,77 C133,73 134,69 132,64 Z" fill="var(--paper)"/>
      <path d="M132,78 C135,81 136,84 136,86 C136,89 134,90 132,90 C130,90 128,89 128,86 C128,83 130,81 132,78 Z" fill="var(--orange)"/>
      <text class="hex-label hex-label-large" x="132" y="110">Burn</text>
      <text class="hex-label hex-label-large" x="132" y="124">Fat</text>

      <!-- heart with pulse -->
      <path d="M201,30 C196,22 184,24 185,34 C186,41 195,46 201,51 C207,46 216,41 217,34 C218,24 206,22 201,30 Z" fill="var(--paper)"/>
      <polyline points="188,37 194,37 197,31 201,42 204,35 214,35" fill="none" stroke="var(--orange)" stroke-width="2"/>
      <text class="hex-label hex-label-small" x="201" y="66">Increase</text>
      <text class="hex-label hex-label-small" x="201" y="80">Endurance</text>

      <!-- recover arrows -->
      <g fill="none" stroke="var(--paper)" stroke-width="3.5">
        <path d="M261,74 A11,11 0 0 1 278,67"/>
        <path d="M282,80 A11,11 0 0 1 265,87"/>
      </g>
      <polygon points="282,62 283,73 273,71" fill="var(--paper)"/>
      <polygon points="261,92 260,81 270,83" fill="var(--paper)"/>
      <text class="hex-label hex-label-large" x="271" y="108">Recover</text>
      <text class="hex-label hex-label-large" x="271" y="122">Faster</text>
    </svg>

    <ul class="benefit-list">
      <li>Promotes Fat Loss*</li>
      <li>Helps Convert Fat Into Energy*</li>
      <li>Promotes Increased Metabolism*</li>
      <li>Promotes Increased Energy*</li>
      <li>Stimulant Free*</li>
    </ul>

    <div class="info-notch"></div>
    <section class="info-panel">
      <h2 class="info-heading info-directions">Directions for use</h2>
      <h2 class="info-heading info-ingredients">Ingredients</h2>
      <h2 class="info-heading info-developer">Developed by</h2>
    </section>
  </div>
</body>
</html>
```